Coffeeshop menu for filter tip

We want to have a cannabis (coffeeshop) menu in the size 25mm wide x 60mm wide. Some examples attached.

it must have the following text:
Menu

WEED p/g
Velotrine €16
Cinderfox €14
Tide Rambler €14
Marigolden €16
Grand Pelican €14
Copper Comet €14

HASH p/g
Baltic Ember €12
Harbor Velvet€11
Plum Rova €14
Dusk Maple €10

Target Market(s)

tourist in Amsterdam

Requirements
Nice to have
• cannabis sign leaf
• No Cigarettes allowed symbol

```html
<!DOCTYPE html>
<html lang="en">
<head>
<meta charset="utf-8">
<title>Amsterdam Menu</title>
<link href="https://fonts.googleapis.com/css2?family=Arimo:wght@400;700&display=swap" rel="stylesheet">
<style>
  :root {
    --paper: #e6e7e9;
    --ink: #020405;
    --amber: #fbaa1f;
    --white: #ffffff;
    --signal-red: #e21e26;
  }
  * { margin: 0; padding: 0; box-sizing: border-box; }
  html, body { width: 1200px; height: 2878px; overflow: hidden; }
  body {
    background: var(--paper);
    font-family: "Arimo", Arial, sans-serif;
    color: var(--ink);
    position: relative;
  }
  .city {
    position: absolute; top: 92px; left: 0; width: 1200px;
    text-align: center; font-weight: 700; font-size: 108px;
    letter-spacing: 38px; padding-left: 38px; line-height: 1;
  }
  .title {
    position: absolute; top: 226px; left: 0; width: 1200px;
    text-align: center; font-weight: 700; font-size: 164px;
    letter-spacing: 40px; padding-left: 40px; line-height: 1;
  }
  .section-band {
    position: absolute; left: 0; width: 1200px; height: 191px;
    background: var(--ink); color: var(--amber);
    font-weight: 700; display: flex; justify-content: space-between;
    align-items: center; padding: 0 56px 0 61px;
  }
  .section-name { font-size: 158px; letter-spacing: 22px; line-height: 1; }
  .unit { font-size: 136px; letter-spacing: 8px; line-height: 1; margin-top: -20px; }
  .weed-band { top: 482px; }
  .hash-band { top: 1589px; }
  .price-list {
    position: absolute; left: 0; width: 1200px; list-style: none;
    padding: 0 52px 0 58px;
  }
  .weed-list { top: 706px; }
  .hash-list { top: 1830px; }
  .price-row {
    display: flex; justify-content: space-between; align-items: baseline;
    gap: 40px; height: 144px; line-height: 1;
  }
  .item-name {
    font-size: 118px; letter-spacing: 1px; white-space: nowrap;
  }
  .price {
    font-size: 124px; letter-spacing: 6px; white-space: nowrap;
    flex: none; width: 220px; text-align: right;
  }
  .notice-band {
    position: absolute; left: 0; top: 2487px; width: 1200px; height: 391px;
    background: var(--ink); display: flex; align-items: center;
    padding-left: 80px;
  }
  .no-smoking { width: 244px; height: 244px; flex: none; }
  .notice-text {
    color: var(--white); font-size: 96px; letter-spacing: 9px;
    margin-left: 72px; line-height: 1; white-space: nowrap;
  }
</style>
</head>
<body>
  <header>
    <div class="city">AMSTERDAM</div>
    <h1 class="title">MENU</h1>
  </header>

  <div class="section-band weed-band"><span class="section-name">WEED</span><span class="unit">p/g</span></div>
  <ul class="price-list weed-list">
    <li class="price-row"><span class="item-name">Velotrine</span><span class="price">€16</span></li>
    <li class="price-row"><span class="item-name">Cinderfox</span><span class="price">€14</span></li>
    <li class="price-row"><span class="item-name">Tide Rambler</span><span class="price">€14</span></li>
    <li class="price-row"><span class="item-name">Marigolden</span><span class="price">€16</span></li>
    <li class="price-row"><span class="item-name">Grand Pelican</span><span class="price">€14</span></li>
    <li class="price-row"><span class="item-name">Copper Comet</span><span class="price">€14</span></li>
  </ul>

  <div class="section-band hash-band"><span class="section-name">HASH</span><span class="unit">p/g</span></div>
  <ul class="price-list hash-list">
    <li class="price-row"><span class="item-name">Baltic Ember</span><span class="price">€12</span></li>
    <li class="price-row"><span class="item-name">Harbor Velvet</span><span class="price">€11</span></li>
    <li class="price-row"><span class="item-name">Plum Rova</span><span class="price">€14</span></li>
    <li class="price-row"><span class="item-name">Dusk Maple</span><span class="price">€10</span></li>
  </ul>

  <footer class="notice-band">
    <svg class="no-smoking" viewBox="0 0 244 244" aria-label="No smoking sign">
      <circle cx="122" cy="122" r="122" fill="var(--signal-red)"/>
      <circle cx="122" cy="122" r="100" fill="var(--white)"/>
      <rect x="40" y="144" width="140" height="26" fill="var(--ink)"/>
      <rect x="184" y="144" width="8" height="26" fill="var(--ink)"/>
      <rect x="196" y="144" width="8" height="26" fill="var(--ink)"/>
      <path d="M188 138 V110 Q188 96 174 94 Q160 92 160 78 Q160 62 176 58" fill="none" stroke="var(--ink)" stroke-width="7"/>
      <path d="M200 138 V108 Q200 86 182 84 Q170 82 172 70" fill="none" stroke="var(--ink)" stroke-width="7"/>
      <line x1="52" y1="52" x2="192" y2="192" stroke="var(--signal-red)" stroke-width="22"/>
    </svg>
    <span class="notice-text">No Cigarettes</span>
  </footer>
</body>
</html>
```